Cover-Design für Collegeblockserie
Zielgruppe
Wir sind ein Anbieter von Papierprodukten wie Hefte, Collegeblöcke und gebundene Bücher für den Schul- und Officebereich. In jedem Jahr bringne wir eine Collegeblockserie heraus mit einem limitierten Coverdesign.
Weitere Infos zu uns und der Aufgabe können dem beigefügten Briefing entnommen werden.
Aufgabenstellung
Vorgaben können dem Breifing entnommen werden

```html
<!DOCTYPE html>
<html lang="de">
<head>
<meta charset="utf-8">
<title>Collegeblock Cover – Be strong</title>
<link rel="stylesheet" href="https://fonts.googleapis.com/css2?family=Dancing+Script:wght@500&display=swap">
<style>
  :root {
    --stage: #f5f5f6;
    --cover-base: #e4e9f4;
    --cover-wash: #d5ddef;
    --teal: #6f9ea3;
    --teal-light: #8fb4b8;
    --ink: #4b4a5a;
    --line-pattern: #9a9aa6;
    --stripe-box: #8a8ba4;
    --circle: #ffffff;
    --avocado-dark: #4c8a2c;
    --avocado-light: #c4d96a;
    --brand: #2f1f8c;
  }
  html, body {
    margin: 0;
    width: 1200px;
    height: 1200px;
    overflow: hidden;
    background: var(--stage);
  }
  .canvas { display: block; width: 1200px; height: 1200px; }
  .cover-base { fill: var(--cover-base); }
  .cover-wash { fill: var(--cover-wash); }
  .ring-patch { fill: url(#ringTone); }
  .line-pattern { fill: var(--line-pattern); opacity: .55; }
  .stripe-box { fill: var(--stripe-box); opacity: .8; }
  .focus-circle { fill: var(--circle); }
  .mascot { fill: url(#avocadoTone); }
  .brand-mark { fill: var(--brand); }
  .brand-name {
    fill: var(--brand);
    font-family: "Dancing Script", cursive;
    font-weight: 500;
    font-size: 40px;
  }
  .slogan {
    fill: var(--ink);
    font-family: "Dancing Script", cursive;
    font-weight: 500;
    font-size: 104px;
  }
</style>
</head>
<body>
<svg class="canvas" viewBox="0 0 1200 1200" xmlns="http://www.w3.org/2000/svg">
  <defs>
    <linearGradient id="ringTone" x1="0" y1="0" x2="1" y2="1">
      <stop offset="0" stop-color="var(--teal)"/>
      <stop offset="1" stop-color="var(--teal-light)"/>
    </linearGradient>
    <linearGradient id="avocadoTone" x1="0" y1="0" x2="0" y2="1">
      <stop offset="0" stop-color="var(--avocado-light)"/>
      <stop offset="1" stop-color="var(--avocado-dark)"/>
    </linearGradient>
  </defs>

  <g class="cover">
    <rect class="cover-base" x="212" y="40" width="776" height="1120"/>
    <path class="cover-wash" d="M585 40 H988 V1160 H690 C640 900 600 600 585 40 Z"/>

    <rect class="ring-patch" x="688" y="61" width="300" height="374" role="img"
          aria-label="Abstraktes Motiv: türkisfarbene Fläche mit weißen, handgezeichneten konzentrischen Ringen"/>

    <rect class="line-pattern" x="223" y="422" width="466" height="257" role="img"
          aria-label="Dekoratives Muster aus dunklen, leicht welligen senkrechten Linien"/>

    <rect class="stripe-box" x="851" y="734" width="137" height="426" role="img"
          aria-label="Dekoratives Muster aus grauvioletten waagerechten Streifen"/>

    <circle class="focus-circle" cx="430" cy="889" r="207"/>

    <rect class="mascot" x="411" y="378" width="378" height="451" rx="140" role="img"
          aria-label="Illustration: fröhliche Avocado mit Kern, die zwei hellblaue Hanteln stemmt"/>

    <g class="brand">
      <rect class="brand-mark" x="322" y="196" width="26" height="26"/>
      <text class="brand-name" x="358" y="220">Kestrel</text>
    </g>

    <text class="slogan" x="287" y="942">Be strong</text>
  </g>
</svg>
</body>
</html>
```